Bottle Labels for Beer (Cherry Beer)

The goal is to design an interesting labeling for a 0,33l bottle for a German beer. The bottle has three labels in total: front, back and "neckholder". The product that is relevant in the first shot is a cherry beer. Only this one is asked to design right now. The further labels will be designed later on as carry-on projects on ArtHive with the chosen design as framework.

Nevertheless the label now will affect the other labels later on for the beers. The label should contain a part that connects all beers to each other. This may be e.g. a part of the canvas that is stable across all front side labels, a character that repeats across all labels or something that connects in any other way the labels later on together. There should not just be simple systematic of a label that changes the colour to distinguish between the different kinds of beer later as the CI color palette limits this. Some beers have one label and then do it in red, green, brown, blue etc. to distinguish between the kinds. It is ok to reference to the beer's colour and a blue, white, black or, wood or paper colour change may be helpful to distinguish. The range of beers that will be introduced are at least for cherry (right now), honey beer, pale ale, IPA, amber, dark, pilsener.

FRONT LABEL
The label should contain the full logo or just the "B". If inconvenient, the label can come also without the logo or "B" when reflected strongly in the upper "neckholder label".

NECKHOLDER LABEL
The neckholder label is a front-side label at the bottleneck. I'm fine if this shows just the logo and nothing else. If you got great other ideas, just go for it.

BACKSIDE LABEL
The appearance on the backside label should enable a co-branding as some beers are done in co-operation with others (in this particular case with the cherry producers and their PVL logo with the cherries). If you split the label in half or put the two logos ("B" and PVL") together as they are both round, is up to you. A positioning in front of the company name might also be an option.
The general Idea is that the backside label is constant across all products (except text and specifications) and just the part for the supporter/partner changes. The backside label has to include the standard objects like EAN barcode, ingredients, net filling content etc.

THE BRAND
The CI colours or themes should be followed where possible. Colours out of CI may be used e.g. the red to relate to the cherry or display of a cherry. Other exeption is the part on the backside where the logo of the partner is shown. Some preferences: round better than cubism, handcraft better than high tech, nature better than industry.

The max. size of the labels is fixed due to technical reasons. Nevertheless, parts of the label may be printed dark brown as the bottle's colour to offer e.g. the appearance of a round label.

The files that describe some hints as well as the text are

I hope, you git interested inn this project and the upcoming designs for the other beers afterwards. For questions, just let me know. Thanks in advance!

Matthias

Target Market(s)

only local / regional customers for the cherry beer and tourists that visit one of the biggest cherry growing regions in Europe.

Requirements
Must have
• A reference to Falkmanns on at least one of the frontside labels. This can be the full logo with text falcons and the "B" of just the "B" if a discrete reference might be a better fit.
Nice to have
• declaration table that provides deeper insight in the specifics of the product for "insiders" like bitter units, alcohol, hops used etc.
Should not have
• too many colours. For the pallet dark blue to white and black to white feel free; green is to avoide, red may be used in this specific case as an exception to underline that it is a cherry beer.

```html
<!DOCTYPE html>
<html lang="de">
<head>
<meta charset="utf-8">
<title>Falkmanns Kirschbier – Etiketten</title>
<link rel="stylesheet" href="https://fonts.googleapis.com/css2?family=Oswald:wght@500;700&family=Open+Sans:wght@400;600&display=swap">
<style>
  :root {
    --paper: #ececec;
    --band: #1b1b1b;
    --band-light: #2a2a2a;
    --ink: #111111;
    --white: #f4f4f4;
    --rule: #d6d6d6;
    --muted: #9a9a9a;
    --cherry: #b5182b;
  }
  * { box-sizing: border-box; margin: 0; padding: 0; }
  html, body { width: 812px; height: 1200px; overflow: hidden; }
  body {
    background: radial-gradient(ellipse at 50% 30%, #fafafa 0%, var(--paper) 70%);
    font-family: "Open Sans", Arial, sans-serif;
    color: var(--white);
    position: relative;
  }

  /* ---------- neck labels ---------- */
  .neck-row {
    position: absolute; top: 44px; left: 0; width: 100%;
    display: flex; justify-content: center; gap: 60px;
  }
  .neck-label {
    width: 220px; height: 110px;
    background: linear-gradient(180deg, var(--band-light), var(--band));
    display: flex; align-items: center; justify-content: center;
  }
  .brand-mark {
    display: flex; align-items: center; gap: 8px;
    font-family: "Oswald", Arial, sans-serif; font-weight: 700;
    color: var(--white); letter-spacing: 1px; text-transform: uppercase;
    line-height: 1;
  }
  .brand-mark .dot { border: 3px solid var(--white); border-radius: 50%; flex: none; }
  .neck-label .brand-mark { font-size: 22px; }
  .neck-label .dot { width: 30px; height: 30px; }

  /* ---------- front label ---------- */
  .front-label { position: absolute; top: 200px; left: 46px; width: 720px; height: 440px; }
  .front-band {
    position: absolute; left: 0; bottom: 0; width: 100%; height: 290px;
    background: linear-gradient(180deg, var(--band-light), var(--band) 60%);
    border-top: 6px solid var(--rule); border-bottom: 6px solid var(--rule);
    outline: 3px solid var(--band); outline-offset: -12px;
  }
  .skyline {
    position: absolute; left: 150px; right: 150px; bottom: 80px; height: 50px;
    background: linear-gradient(180deg, rgba(255,255,255,0) 0%, rgba(255,255,255,0.1) 100%);
  }
  .front-badge {
    position: absolute; top: 0; left: 50%; transform: translateX(-50%);
    width: 340px; height: 340px; border-radius: 50%;
    background: var(--band); border: 3px solid #555; z-index: 2;
    display: flex; align-items: center; justify-content: center;
  }
  .front-badge .ring {
    width: 300px; height: 300px; border-radius: 50%;
    border: 12px solid var(--white); background: var(--ink);
    display: flex; flex-direction: column; align-items: center; justify-content: center; gap: 10px;
  }
  .badge-art-top {
    width: 170px; height: 62px; border-radius: 31px;
    background: linear-gradient(180deg, #6a6a6a, #2c2c2c);
  }
  .front-badge .brand-mark { font-size: 42px; }
  .front-badge .dot { width: 20px; height: 20px; }
  .badge-rule { width: 190px; height: 2px; background: var(--white); }
  .badge-art-bottom {
    width: 96px; height: 58px; border-radius: 10px 10px 4px 4px;
    background: linear-gradient(180deg, #e8e8e8, #8a8a8a);
  }
  .front-meta {
    position: absolute; bottom: 22px; left: 30px; right: 30px;
    display: flex; justify-content: space-between; align-items: flex-end;
    font-size: 16px; color: #cfcfcf; line-height: 1.2;
  }
  .front-center {
    position: absolute; left: 50%; transform: translateX(-50%); bottom: 16px;
    display: flex; flex-direction: column; align-items: center; gap: 8px;
  }
  .tagline {
    font-family: "Oswald", Arial, sans-serif; font-weight: 500;
    letter-spacing: 8px; font-size: 18px; color: #d8d8d8; line-height: 1;
    white-space: nowrap;
  }
  .cherry-icon { width: 22px; height: 26px; flex: none; }

  /* ---------- back label ---------- */
  .back-label { position: absolute; top: 680px; left: 46px; width: 720px; height: 480px; }
  .back-badge {
    position: absolute; top: 0; left: 50%; transform: translateX(-50%);
    width: 150px; height: 150px; border-radius: 50%;
    background: var(--band); border: 2px solid #555; z-index: 2;
    display: flex; align-items: center; justify-content: center;
  }
  .back-badge .ring {
    width: 130px; height: 130px; border-radius: 50%;
    border: 5px solid var(--white); background: var(--ink);
    display: flex; align-items: center; justify-content: center;
  }
  .back-badge .brand-mark { font-size: 17px; gap: 5px; }
  .back-badge .dot { width: 10px; height: 10px; border-width: 2px; }
  .back-band {
    position: absolute; left: 0; top: 60px; width: 100%; height: 410px;
    background: linear-gradient(180deg, var(--band-light), var(--band) 60%);
    border-top: 6px solid var(--rule); border-bottom: 6px solid var(--rule);
    outline: 3px solid var(--band); outline-offset: -12px;
    padding: 100px 40px 18px;
    display: flex; flex-direction: column;
  }
  .region-name {
    text-align: center; font-size: 22px; color: var(--cherry); font-weight: 600;
    line-height: 1.2; margin-bottom: 10px;
  }
  .description { font-size: 12.5px; line-height: 1.5; text-align: justify; color: #e6e6e6; }
  .back-band .tagline { text-align: center; font-size: 13px; margin: 12px 0 12px; }
  .declaration { display: flex; gap: 20px; font-size: 10.5px; line-height: 1.55; color: #cfcfcf; }
  .declaration .specs { flex: 1; }
  .declaration .producer { flex: 1.3; border-left: 1px solid #555; padding-left: 16px; }
  .back-icons {
    margin-top: auto; padding-top: 8px;
    display: flex; align-items: center; gap: 30px;
  }
  .icon-warning { width: 28px; height: 28px; border-radius: 50%; background: var(--white); border: 4px solid var(--cherry); flex: none; }
  .icon-seal { width: 30px; height: 30px; border-radius: 50%; border: 2px solid #bbb; flex: none; }
  .partner-mark {
    display: flex; align-items: center; gap: 6px;
    font-family: "Oswald", Arial, sans-serif; font-weight: 700; font-size: 16px; color: var(--white);
  }
  .partner-mark .dot { width: 14px; height: 14px; border-radius: 50%; border: 2px solid var(--white); }
  .back-icons .cherry-icon { margin-left: auto; }
</style>
</head>
<body>

  <section class="neck-row">
    <div class="neck-label">
      <div class="brand-mark"><span class="dot"></span>Falkmanns</div>
    </div>
    <div class="neck-label">
      <div class="brand-mark"><span class="dot"></span>Falkmanns</div>
    </div>
  </section>

  <section class="front-label">
    <div class="front-band">
      <div class="skyline" role="img" aria-label="Faint town skyline drawing"></div>
      <div class="front-meta">
        <div>375ML<br>7.5ALC</div>
        <div>e0,33L</div>
      </div>
      <div class="front-center">
        <div class="tagline">GERMAN BEER</div>
        <svg class="cherry-icon" viewBox="0 0 26 30" aria-hidden="true">
          <path d="M8 20 Q12 6 20 2 M20 2 Q19 12 19 20" stroke="#f4f4f4" stroke-width="1.6" fill="none"/>
          <circle cx="7" cy="23" r="6" fill="#f4f4f4"/>
          <circle cx="19" cy="23" r="6" fill="#f4f4f4"/>
        </svg>
      </div>
    </div>
    <div class="front-badge">
      <div class="ring">
        <div class="badge-art-top" role="img" aria-label="Two falcon heads with hop cones"></div>
        <div class="brand-mark"><span class="dot"></span>Falkmanns</div>
        <div class="badge-rule"></div>
        <div class="badge-art-bottom" role="img" aria-label="Copper brew kettle drawing"></div>
      </div>
    </div>
  </section>

  <section class="back-label">
    <div class="back-badge">
      <div class="ring">
        <div class="brand-mark"><span class="dot"></span>Falkmanns</div>
      </div>
    </div>
    <div class="back-band">
      <p class="region-name">Hügelland Nordtal</p>
      <p class="description">Durch das Aroma der Hopfensorten und die obergärige Hefe bekommt Kirschling einen erfrischenden Geschmack mit Noten von Vanille, Zitrusfrüchten und Beerenobst; der Fruchtcharakter wird durch den Kirschsaft noch unterstützt und kommt ohne Zuckerzusätze aus.</p>
      <p class="tagline">GERMAN BEER</p>
      <div class="declaration">
        <div class="specs">
          ALC. 4,7 %<br>PLATO 11,2<br>IBU 27<br>CONT. 0,33l<br>
          Hopfen: Perle, Select, Ariana, Hbc Pure<br>Genusstemp.: 9 °C
        </div>
        <div class="producer">
          Zutaten: Wasser, Malz, Hopfen, Kirschsaft, Hefe<br>
          Falkmanns Braumanufaktur<br>
          DE-34999 Talheim · www.falkmanns.example<br>
          Obstgenossenschaft Talgrund eG<br>
          DE-37999 Kirschdorf · www.pvl-kirschen.example<br>
          Mindestens haltbar bis 15.06.2018
        </div>
      </div>
      <div class="back-icons">
        <span class="icon-warning" role="img" aria-label="Hinweiszeichen"></span>
        <span class="icon-seal" role="img" aria-label="Qualitätssiegel"></span>
        <div class="partner-mark"><span class="dot"></span>PVL</div>
        <svg class="cherry-icon" viewBox="0 0 26 30" aria-hidden="true">
          <path d="M8 20 Q12 6 20 2 M20 2 Q19 12 19 20" stroke="#f4f4f4" stroke-width="1.6" fill="none"/>
          <circle cx="7" cy="23" r="6" fill="#f4f4f4"/>
          <circle cx="19" cy="23" r="6" fill="#f4f4f4"/>
        </svg>
      </div>
    </div>
  </section>

</body>
</html>
```